A Global Agro-Commodities Trading Company with HQ in UAE wishes to redesign its Stationery

Creative Brief

Company Profile:
Velmor Crop Group is head-quartered in Dubai, United Arab Emirates and specializes in supply chain management of agricultural commodities such as Pulses, Oil Seeds & Edible Oils, Frozen Poultry & Meats, Dairy Products, Animal Feed Raw Materials, Spices, Staples, Dried Fruits, Various Jute Products, Packaging Materials and Special Crops. Velmor Crop’s strategically located network of 24 overseas offices, warehouses, processing and logistics facilities currently exports 54 different food products from 52 countries to over 1000 customers in 82 countries.

Objective:
Design office stationery (Business Cards and Letterheads) such that it provides all the necessary information, gives a corporate feel and is aesthetic. Our current business card template appears cluttered as it has all the information on one side and the Arabic translation on the other. To get rid of the clutter and to make it “easy on the eyes”, we have decided against the Arabic translation and present our global outreach (presence in 24 countries worldwide), in its place.

Key Elements:
- Logo (attached)
- Pantone 285 C (blue) is our official corporate colour. However, we are willing to look at options that have some other subtle colours added to the design to make it look appealing (any other colour added should give a corporate/professional feel)
- We would like to include the following information on the new card:
1. Full Name
2. Designation
3. Company Name
4. Address
5. Company Tel No
6. Fax No
7. Mobile No
8. Email address
9. Website
10. A visual depiction of our presence in 24 countries (a map maybe?) at the back of the card
11. A QR code

We have made an initial start on the redesign in-house using Photoshop, but due to the creative limitations in PS we have decided to seek concepts through Sketch Hive to help us finalise this project using programs more equipped for this work. For your use and information we have attached the following:
• Current business card template
• Drafts and proposed concepts for the new look
We trust that participants will be able to extend on the drafts with innovative, creative and concise concepts and ideas.
We look forward to your participation and thank you in advance for your creative input

Industry/Entity Type

Requirements
Must have
• We would like to include the following information on the new card:
• 1. Full Name
• 2. Designation
• 3. Company Name
• 4. Address
• 5. Company Tel No
• 6. Fax No
• 7. Mobile No
• 8. Email address
• 9. Website
• 10. A visual depiction of our presence in 24 countries (a map maybe?) at the back of the card
• 11. A QR code
Nice to have
• subtle use of an additional color/s (1 - 2) ...Company color Pantone 285C
Should not have
• Enlargement of the logo sun....

```html
<!DOCTYPE html>
<html lang="en">
<head>
<meta charset="utf-8">
<title>Velmor Crop Group — Stationery</title>
<link href="https://fonts.googleapis.com/css2?family=Arimo:wght@400;700&display=swap" rel="stylesheet">
<style>
  :root{
    --brand-blue:#1a6fba;
    --brand-blue-light:#cfe0f1;
    --curve-grey:#b4b6ba;
    --paper:#ffffff;
    --stage:#ececec;
    --ink:#3a3a3a;
  }
  *{margin:0;padding:0;box-sizing:border-box}
  html,body{width:1200px;height:937px;overflow:hidden}
  body{background:var(--stage);position:relative;font-family:"Arimo",Arial,sans-serif;color:var(--ink)}
  .sheet{position:absolute;background:var(--paper);overflow:hidden;box-shadow:0 1px 3px rgba(0,0,0,.12)}
  .sheet .band{position:absolute;inset:0;width:100%;height:100%}
  .wordmark{position:absolute;display:flex;align-items:center;gap:.3em;color:var(--brand-blue);font-weight:700;letter-spacing:.02em;line-height:1;white-space:nowrap}
  .wordmark .dot{width:.7em;height:.7em;border-radius:50%;background:var(--brand-blue)}

  /* Letterhead */
  .letterhead{left:185px;top:67px;width:384px;height:545px}
  .letterhead .wordmark{left:22px;top:32px;font-size:22px}
  .letter{position:absolute;left:28px;top:140px;width:290px;font-size:5.4px;line-height:1.55;color:var(--ink)}
  .letter p{margin-bottom:9px}
  .letter .greet{font-weight:700;margin-bottom:0}
  .signature{width:22px;height:14px;background:#d6d6d6;border-radius:2px;margin:4px 0 6px}
  .signer{font-weight:700}
  .letter-footer{position:absolute;left:28px;top:462px;font-size:4.8px;line-height:1.7;color:var(--ink)}
  .letter-footer strong{display:block}

  /* Folder */
  .folder{left:636px;top:41px;width:458px;height:575px}
  .folder .wordmark{left:72px;top:292px;font-size:46px}

  /* Business cards */
  .card{width:177px;height:100px;border-radius:8px}
  .card-front{left:45px;top:658px}
  .card-front .wordmark{left:9px;top:42px;font-size:13px}
  .card-details{position:absolute;right:8px;top:8px;text-align:right;color:#fff;font-size:4.6px;line-height:1.5}
  .card-details .name{font-size:5.6px;font-weight:700;letter-spacing:.05em}
  .card-details .gap{height:6px}
  .card-back{left:45px;top:784px}
  .presence-map{position:absolute;left:8px;top:18px;width:150px;height:64px;border-radius:6px;background:linear-gradient(90deg,var(--brand-blue-light) 0%,var(--brand-blue-light) 50%,rgba(255,255,255,.28) 50%,rgba(255,255,255,.28) 100%)}
  .qr-code{position:absolute;right:8px;bottom:8px;width:26px;height:26px;background:#fff;border-radius:2px}

  /* Envelope front */
  .envelope-front{left:265px;top:672px;width:431px;height:208px}
  .envelope-front .wordmark{left:22px;top:26px;font-size:20px}

  /* Envelope back */
  .envelope-back{left:737px;top:672px;width:431px;height:208px}
  .flap{position:absolute;left:0;top:0;width:100%;height:72px;background:var(--brand-blue);border-bottom-left-radius:60px 44px;border-bottom-right-radius:14px}
  .site{position:absolute;left:0;right:0;top:28px;text-align:center;color:#fff;font-size:12px;letter-spacing:.18em}
</style>
</head>
<body>

<section class="sheet letterhead">
  <svg class="band" viewBox="0 0 100 100" preserveAspectRatio="none" aria-hidden="true">
    <path d="M92,0 C79,25 79,45 87,60 C93,72 85,86 83,100 L100,100 L100,0Z" fill="var(--curve-grey)"/>
    <path d="M94,0 C82,25 82,45 90,60 C96,72 88,86 86,100 L100,100 L100,0Z" fill="var(--brand-blue)"/>
  </svg>
  <div class="wordmark"><span class="dot"></span>Velmor</div>
  <div class="letter">
    <p>July 2, 2012</p>
    <p class="greet">Dear Sir,</p>
    <p>ABC Building, Main St., Country Name</p>
    <p>is simply dummy text of the printing and typesetting industry. Lorem Ipsum has been the industry's standard dummy text ever since the 1500s, when an unknown printer took a galley of type and scrambled it to make a type specimen book. It has survived not only five centuries, but also the leap into electronic typesetting, remaining essentially unchanged. It was popularised in the 1960s with the release of sheets containing Lorem Ipsum passages, and more recently with desktop publishing software including versions of Lorem Ipsum.</p>
    <p>is simply dummy text of the printing and typesetting industry. Lorem Ipsum has been the industry's standard dummy text ever since the 1500s, when an unknown printer took a galley of type and scrambled it to make</p>
    <p>is simply dummy text of the printing and typesetting industry. Lorem Ipsum has been the industry's standard dummy text ever since the 1500s, when an unknown printer took a galley of type and scrambled it to make a type specimen book. It has survived not only five centuries, but also the leap into electronic typesetting, remaining essentially unchanged. It was popularised in the 1960s with the release of sheets containing Lorem Ipsum passages, and more recently with desktop publishing software including versions of Lorem Ipsum.</p>
    <p style="margin-bottom:2px">Best Regards,</p>
    <div class="signature" role="img" aria-label="Handwritten signature"></div>
    <div class="signer">Daniel Kerr</div>
    <div>Director</div>
    <div style="margin-top:3px">ABC Building, Main St., Country Name</div>
  </div>
  <div class="letter-footer">
    <strong>Unit 58, Trade Tower</strong>
    <strong>Business Bay, Dubai</strong>
    <div>☏ +971 4 555 0187</div>
    <div>▯ +971 4 555 0188</div>
    <div>☏ +971 4 555 0189</div>
    <div>✉ info@velmorcrop.com</div>
    <div>◍ www.velmorcrop.com</div>
  </div>
</section>

<section class="sheet folder">
  <svg class="band" viewBox="0 0 100 100" preserveAspectRatio="none" aria-hidden="true">
    <path d="M83,0 C93,20 91,40 84,55 C77,72 80,88 84,100 L100,100 L100,0Z" fill="var(--curve-grey)"/>
    <path d="M86,0 C96,20 94,40 87,55 C80,72 83,88 87,100 L100,100 L100,0Z" fill="var(--brand-blue)"/>
  </svg>
  <div class="wordmark"><span class="dot"></span>Velmor</div>
</section>

<section class="sheet card card-front">
  <svg class="band" viewBox="0 0 100 100" preserveAspectRatio="none" aria-hidden="true">
    <path d="M49,0 C43,30 43,65 50,100 L100,100 L100,0Z" fill="var(--curve-grey)"/>
    <path d="M52,0 C46,30 46,65 53,100 L100,100 L100,0Z" fill="var(--brand-blue)"/>
  </svg>
  <div class="wordmark"><span class="dot"></span>Velmor</div>
  <div class="card-details">
    <div class="name">ROWAN ELLIS</div>
    <div>Managing Director</div>
    <div class="gap"></div>
    <div>Unit 58, Trade Tower</div>
    <div>Business Bay, Dubai</div>
    <div class="gap"></div>
    <div>+971 4 555 0187 ☏</div>
    <div>+971 4 555 0188 ▯</div>
    <div>+971 4 555 0189 ☏</div>
    <div>info@velmorcrop.com ✉</div>
    <div>www.velmorcrop.com ◍</div>
  </div>
</section>

<section class="sheet card card-back">
  <svg class="band" viewBox="0 0 100 100" preserveAspectRatio="none" aria-hidden="true">
    <rect x="50" y="0" width="50" height="100" fill="var(--brand-blue)"/>
  </svg>
  <div class="presence-map" role="img" aria-label="World map marking the company's presence in 24 countries"></div>
  <div class="qr-code" role="img" aria-label="QR code linking to the company website"></div>
</section>

<section class="sheet envelope-front">
  <svg class="band" viewBox="0 0 100 100" preserveAspectRatio="none" aria-hidden="true">
    <path d="M93,0 C98,30 97,65 92,100 L100,100 L100,0Z" fill="var(--curve-grey)"/>
    <path d="M94.5,0 C99.5,30 98.5,65 93.5,100 L100,100 L100,0Z" fill="var(--brand-blue)"/>
  </svg>
  <div class="wordmark"><span class="dot"></span>Velmor</div>
</section>

<section class="sheet envelope-back">
  <div class="flap"><div class="site">www.velmorcrop.com</div></div>
</section>

</body>
</html>
```